Personal contact Business card design needed

I work in the Property Industry - specifically Property Management.

I need a card I can hand out to colleagues at networking events, meetings, training courses etc. that will provide my contact details.

Target Market(s)

Professional colleagues / potential clients / employers

Industry/Entity Type

Training

Contact Information for Business Card

I need a simple and professional card to give to professional network contacts at meetings, interviews etc.

The card should include my photograph, name, mobile number, email address and Proflinx address.

I would like appropriate professional colours. Something feminine but not too 'frilly' or 'girly'

Requirements
Must have
• Photograph of myself.
I want it to be simple,perhaps a small icon for each contact detail such as
Email icon
Proflinx icon
Mobile number

```html
<!DOCTYPE html>
<html lang="en">
<head>
<meta charset="utf-8">
<title>Dana Marsh – Business Card</title>
<link rel="stylesheet" href="https://fonts.googleapis.com/css2?family=Oswald:wght@500&family=Open+Sans:wght@400&display=swap">
<style>
  :root {
    --page-bg: #e9e6e2;
    --card-white: #ffffff;
    --band-tint: #f1f2f3;
    --name-teal: #1a8a9c;
    --text-grey: #8a8d90;
    --charcoal: #2c2d2f;
    --stripe-green: #9cc47f;
    --stripe-sage: #7fb39a;
    --stripe-tan: #d9c3a6;
    --stripe-slate: #a3acb6;
    --stripe-purple: #b67fc6;
    --photo-light: #d8d5cf;
    --photo-dark: #3d2a27;
  }
  html, body {
    margin: 0;
    padding: 0;
    width: 1200px;
    height: 1000px;
    overflow: hidden;
    background: var(--page-bg);
  }
  .business-card {
    position: absolute;
    left: 420px;
    top: 180px;
    width: 360px;
    height: 640px;
    background: var(--card-white);
    box-shadow: 0 6px 20px rgba(0,0,0,0.18);
    overflow: hidden;
  }
  .portrait {
    position: absolute;
    left: 0; top: 0;
    width: 360px; height: 336px;
    background: radial-gradient(ellipse 45% 60% at 55% 70%, var(--photo-dark) 0%, #5a423c 45%, var(--photo-light) 75%);
  }
  .stripe-row {
    position: absolute;
    left: 0;
    width: 360px;
    height: 8px;
    display: flex;
  }
  .stripe-row span { flex: 1; }
  .stripe-row span + span { margin-left: 14px; }
  .stripe-row.top { top: 336px; }
  .stripe-row.bottom { top: 522px; }
  .stripe-green { background: var(--stripe-green); }
  .stripe-sage { background: var(--stripe-sage); }
  .stripe-tan { background: var(--stripe-tan); }
  .stripe-slate { background: var(--stripe-slate); }
  .stripe-purple { background: var(--stripe-purple); }
  .info-band {
    position: absolute;
    left: 0; top: 344px;
    width: 360px; height: 178px;
    background: linear-gradient(180deg, var(--card-white) 0%, var(--band-tint) 100%);
  }
  .holder-name {
    position: absolute;
    right: 34px;
    top: 22px;
    margin: 0;
    font-family: "Oswald", sans-serif;
    font-weight: 500;
    font-size: 44px;
    line-height: 1;
    letter-spacing: 0.5px;
    color: var(--name-teal);
  }
  .contact-list {
    position: absolute;
    left: 52px;
    top: 92px;
    margin: 0;
    padding: 0;
    list-style: none;
    font-family: "Open Sans", sans-serif;
    font-size: 14px;
    color: var(--text-grey);
  }
  .contact-list li {
    display: flex;
    align-items: center;
    height: 24px;
  }
  .contact-list svg {
    width: 12px;
    height: 12px;
    margin-right: 8px;
    fill: var(--text-grey);
    flex: none;
  }
  .footer-panel {
    position: absolute;
    left: 0; top: 530px;
    width: 360px; height: 110px;
    background: var(--charcoal);
  }
</style>
</head>
<body>
  <div class="business-card">
    <div class="portrait" role="img" aria-label="Portrait photograph of Dana Marsh, smiling, with long dark hair, against a light grey wall"></div>

    <div class="stripe-row top">
      <span class="stripe-green"></span><span class="stripe-sage"></span><span class="stripe-tan"></span><span class="stripe-slate"></span><span class="stripe-purple"></span>
    </div>

    <div class="info-band">
      <h1 class="holder-name">DANA MARSH</h1>
      <ul class="contact-list">
        <li>
          <svg viewBox="0 0 12 12" aria-hidden="true"><path d="M2.4 0.6 L4.2 2.8 L3.2 4.2 C3.8 5.6 6.4 8.2 7.8 8.8 L9.2 7.8 L11.4 9.6 L10.2 11.2 C6 11.4 0.6 6 0.8 1.8 Z"/></svg>
          0400 512 306
        </li>
        <li>
          <svg viewBox="0 0 12 12" aria-hidden="true"><path d="M0.5 2 H11.5 V10 H0.5 Z M1.4 2.8 L6 6.4 L10.6 2.8" stroke="#ffffff" stroke-width="0.9"/></svg>
          dana@mailbox-example.com.au
        </li>
        <li>
          <svg viewBox="0 0 12 12" aria-hidden="true"><rect x="0.5" y="0.5" width="11" height="11" rx="1.5"/></svg>
          au.proflinx.com/in/danamarshaustralia/
        </li>
      </ul>
    </div>

    <div class="stripe-row bottom">
      <span class="stripe-green"></span><span class="stripe-sage"></span><span class="stripe-tan"></span><span class="stripe-slate"></span><span class="stripe-purple"></span>
    </div>

    <div class="footer-panel"></div>
  </div>
</body>
</html>
```